TALMERA Stationary and Biz Card design
TALMERA Economic Development Company
TALMERA Stationary and Biz Card design - Financial Services
Creative Brief
Professional
Dennis P Wexford
CEO
PO BOX 782 FAIRHOLT, MAINE 04987
dennis@talmeraco.example
talmeraco.example
Looking for designs that encompass the strength and integrity of the logo.

```html
<!DOCTYPE html>
<html lang="en">
<head>
<meta charset="utf-8">
<title>TALMERA Business Card Set</title>
<link rel="stylesheet" href="https://fonts.googleapis.com/css2?family=Montserrat:wght@400;600;700&family=Roboto:wght@400&display=swap">
<style>
  :root{
    --stage:#b78a5e;
    --navy:#1f3566;
    --white:#ffffff;
    --ink:#1f3566;
    --muted:#5a6580;
    --label:#2e2218;
  }
  *{margin:0;padding:0;box-sizing:border-box}
  html,body{width:1200px;height:839px;overflow:hidden}
  body{background:var(--stage);font-family:"Montserrat",sans-serif;position:relative}

  .card{position:absolute;overflow:hidden;box-shadow:0 2px 6px rgba(0,0,0,.25)}
  .card--white{background:var(--white);color:var(--ink)}
  .card--navy{background:var(--navy);color:var(--white)}

  .label{position:absolute;font-family:"Roboto",sans-serif;font-size:17px;color:var(--label);text-align:center}

  .wordmark{position:absolute;font-weight:700;letter-spacing:.2em;white-space:nowrap;line-height:1}
  .web{position:absolute;font-size:8px;letter-spacing:.05em;font-weight:600}

  .person{position:absolute;font-size:9px;letter-spacing:.04em;white-space:nowrap}
  .person .role{font-size:8px;opacity:.8}

  .contacts{position:absolute;list-style:none;font-size:6.5px;line-height:11px;letter-spacing:.03em}
  .contacts li{display:flex;align-items:center;gap:4px;white-space:nowrap}
  .contacts svg{width:6px;height:6px;flex:none}

  .panel{position:absolute;top:0;right:0;bottom:0;background:var(--navy);color:var(--white)}
</style>
</head>
<body>

<!-- Row 1 -->
<section class="card card--white" style="left:216px;top:48px;width:391px;height:187px">
  <div class="wordmark" style="left:36px;top:112px;font-size:24px;color:var(--ink)">TALMERA</div>
  <div class="panel" style="width:170px">
    <div class="person" style="left:14px;top:26px">Dennis P Wexford<br><span class="role">CEO</span></div>
    <ul class="contacts" style="left:14px;top:70px">
      <li><svg viewBox="0 0 6 6"><circle cx="3" cy="3" r="2.5" fill="currentColor"/></svg>207 555 0148</li>
      <li><svg viewBox="0 0 6 6"><circle cx="3" cy="3" r="2.5" fill="currentColor"/></svg>207 555 0192</li>
      <li><svg viewBox="0 0 6 6"><circle cx="3" cy="3" r="2.5" fill="currentColor"/></svg>dennis@talmeraco.example</li>
      <li><svg viewBox="0 0 6 6"><circle cx="3" cy="3" r="2.5" fill="currentColor"/></svg>www.talmeraco.example</li>
      <li><svg viewBox="0 0 6 6"><circle cx="3" cy="3" r="2.5" fill="currentColor"/></svg>PO BOX 782 FAIRHOLT,</li>
      <li style="padding-left:10px">MAINE 04987</li>
    </ul>
  </div>
</section>
<div class="label" style="left:216px;top:250px;width:391px">BC1 Front</div>

<section class="card card--navy" style="left:660px;top:48px;width:324px;height:187px">
  <div class="wordmark" style="left:0;right:0;top:80px;text-align:center;font-size:24px">TALMERA</div>
  <div class="web" style="right:22px;top:150px">www.talmeraco.example</div>
</section>
<div class="label" style="left:660px;top:250px;width:324px">BC1 Back</div>

<!-- Row 2 -->
<section class="card card--white" style="left:84px;top:307px;width:336px;height:185px">
  <div class="person" style="left:22px;top:30px;font-size:10px">Dennis P Wexford <span class="role">| CEO</span></div>
  <div class="wordmark" style="left:22px;top:118px;font-size:20px">TALMERA</div>
  <ul class="contacts" style="left:186px;top:82px;color:var(--muted)">
    <li><svg viewBox="0 0 6 6"><circle cx="3" cy="3" r="2.5" fill="currentColor"/></svg>207 555 0148</li>
    <li><svg viewBox="0 0 6 6"><circle cx="3" cy="3" r="2.5" fill="currentColor"/></svg>207 555 0192</li>
    <li><svg viewBox="0 0 6 6"><circle cx="3" cy="3" r="2.5" fill="currentColor"/></svg>dennis@talmeraco.example</li>
    <li><svg viewBox="0 0 6 6"><circle cx="3" cy="3" r="2.5" fill="currentColor"/></svg>www.talmeraco.example</li>
    <li><svg viewBox="0 0 6 6"><circle cx="3" cy="3" r="2.5" fill="currentColor"/></svg>PO BOX 782 FAIRHOLT,</li>
    <li style="padding-left:10px">MAINE 04987</li>
  </ul>
</section>
<div class="label" style="left:84px;top:508px;width:336px">BC2 Front</div>

<section class="card card--white" style="left:437px;top:307px;width:324px;height:185px">
  <div class="wordmark" style="left:0;right:0;top:80px;text-align:center;font-size:30px">TALMERA</div>
</section>
<div class="label" style="left:437px;top:508px;width:324px">BC2 Back1</div>

<section class="card card--white" style="left:811px;top:307px;width:329px;height:185px">
  <div class="wordmark" style="left:0;right:0;top:72px;text-align:center;font-size:30px">TALMERA</div>
  <div class="web" style="left:0;right:0;top:150px;text-align:center">www.talmeraco.example</div>
</section>
<div class="label" style="left:811px;top:508px;width:329px">BC2 Back2</div>

<!-- Row 3 -->
<section class="card card--navy" style="left:84px;top:564px;width:336px;height:192px">
  <div class="person" style="left:22px;top:30px;font-size:10px">Dennis P Wexford <span class="role">| CEO</span></div>
  <div class="wordmark" style="left:22px;top:124px;font-size:20px">TALMERA</div>
  <ul class="contacts" style="left:186px;top:86px">
    <li><svg viewBox="0 0 6 6"><circle cx="3" cy="3" r="2.5" fill="currentColor"/></svg>207 555 0148</li>
    <li><svg viewBox="0 0 6 6"><circle cx="3" cy="3" r="2.5" fill="currentColor"/></svg>207 555 0192</li>
    <li><svg viewBox="0 0 6 6"><circle cx="3" cy="3" r="2.5" fill="currentColor"/></svg>dennis@talmeraco.example</li>
    <li><svg viewBox="0 0 6 6"><circle cx="3" cy="3" r="2.5" fill="currentColor"/></svg>www.talmeraco.example</li>
    <li><svg viewBox="0 0 6 6"><circle cx="3" cy="3" r="2.5" fill="currentColor"/></svg>PO BOX 782 FAIRHOLT,</li>
    <li style="padding-left:10px">MAINE 04987</li>
  </ul>
</section>
<div class="label" style="left:84px;top:772px;width:336px">BC3 Front</div>

<section class="card card--navy" style="left:437px;top:564px;width:324px;height:192px">
  <div class="wordmark" style="left:0;right:0;top:84px;text-align:center;font-size:30px">TALMERA</div>
</section>
<div class="label" style="left:437px;top:772px;width:324px">BC3 Back1</div>

<section class="card card--navy" style="left:811px;top:564px;width:329px;height:192px">
  <div class="wordmark" style="left:0;right:0;top:76px;text-align:center;font-size:30px">TALMERA</div>
  <div class="web" style="left:0;right:0;top:156px;text-align:center">www.talmeraco.example</div>
</section>
<div class="label" style="left:811px;top:772px;width:329px">BC3 Back2</div>

</body>
</html>
```